Accountancy firm needs clean and simple website and optional logo

We need a logo and basic wordpress website design for a Sydney based accountancy firm.
We need a clean and simple logo and website, based on the accounting/finance/tax industry. Simple, credible and official colors.
The logo is expected to be so simple that we have combined into the one job.
If you submit a logo design and we choose it along with someone else's website design you will be paid a bonus of $60. The website design will still win the competition as per normal.
Current website is old and terrible but gives you an idea of the sitemap (super simple) and what they do: www.brookfiscal.com.au
We want original different to normal template looking designs.
We like videos, and like http://www.whitfords.com.au/
Feel free to go to vidhaven and use some videos from there.
We are based in Sydney Australia and in the field of taxation and accounting
We want a clean, formal, credible site, limited pages.
The project is guaranteed, so go for it.
Brook & Associates
1 page

```html
<!DOCTYPE html>
<html lang="en">
<head>
<meta charset="utf-8">
<title>Brook &amp; Associates — Tax Accountants</title>
<link rel="stylesheet" href="https://fonts.googleapis.com/css2?family=Raleway:wght@400;500;600;700;800&family=Open+Sans:wght@400;600&display=swap">
<style>
:root{
  --blue:#0aa0f5;
  --white:#ffffff;
  --ink:#2b2b2b;
  --grey-band:#c3c3c3;
  --field:#ececec;
  --footer:#000000;
  --brand-panel:#eeeeee;
}
*{box-sizing:border-box;margin:0;padding:0}
html,body{width:1109px;height:1200px;overflow:hidden}
body{position:relative;font-family:"Open Sans",sans-serif;color:var(--white);background:#000}
.abs{position:absolute}
.photo-backdrop{left:0;top:0;width:1109px;height:879px;
  background:linear-gradient(180deg,#4d6e9c 0%,#6a87b0 25%,#8296b4 42%,#7b7f8a 50%,#5d5a55 70%,#4f4c47 100%)}
.service-shade{left:0;top:435px;width:1109px;height:444px;background:rgba(0,0,0,.62)}
.header{left:0;top:0;width:1109px;height:77px;border-bottom:1px solid rgba(255,255,255,.45);background:rgba(60,80,110,.15)}
.brand-panel{left:43px;top:0;width:271px;height:76px;background:var(--brand-panel);display:flex;align-items:center;justify-content:center}
.brand-name{font-family:"Open Sans",sans-serif;font-weight:600;font-size:18px;color:var(--ink);white-space:nowrap}
.nav{top:30px;left:437px;font-family:"Raleway",sans-serif;font-size:11.5px;font-weight:500}
.nav a{color:var(--white);text-decoration:none;position:absolute;white-space:nowrap}
.nav a.active{color:var(--blue)}
.call{left:947px;top:22px;display:flex;gap:10px;align-items:center}
.call-label{font-size:11px;color:var(--blue);line-height:1.2}
.call-number{font-size:13px;color:var(--white)}
.hero-title{left:0;width:1109px;top:142px;text-align:center;font-family:"Raleway",sans-serif;font-weight:700;font-size:88px;letter-spacing:14px;line-height:1}
.hero-sub{left:0;width:1091px;top:235px;text-align:center;font-family:"Raleway",sans-serif;font-weight:400;font-size:52px;line-height:63px}
.slide-arrow{width:37px;height:37px;border:2px solid var(--white);border-radius:50%;top:243px;display:flex;align-items:center;justify-content:center}
.section-title{left:0;width:1134px;text-align:center;font-family:"Raleway",sans-serif;font-weight:700;font-size:33px}
.section-title span{color:var(--blue)}
.timeline{left:225px;top:623px;width:622px;height:2px;background:var(--white)}
.service-icon{width:115px;height:115px;border-radius:50%;top:565px;display:flex;align-items:center;justify-content:center;background:var(--blue)}
.service-icon.is-current{background:var(--white)}
.service{width:330px;top:696px;text-align:center}
.service h3{font-family:"Raleway",sans-serif;font-weight:700;font-size:16px;color:var(--blue);letter-spacing:.2px}
.service p{font-size:11.3px;line-height:15px;margin-top:15px;color:var(--white)}
.service .more{display:inline-block;margin-top:8px;font-size:11.5px;color:var(--white)}
.service .more.is-current{color:var(--blue)}
.newsletter{left:0;top:879px;width:1109px;height:204px;background:var(--grey-band)}
.newsletter .section-title{top:42px;color:var(--ink);font-size:32px;width:1084px}
.field{top:111px;height:47px;background:var(--field);color:#777;font-size:11px;padding:0 14px;display:flex;align-items:center}
.signup{left:813px;top:110px;width:258px;height:47px;background:var(--blue);color:var(--white);font-size:17px;display:flex;align-items:center;justify-content:center;font-family:"Raleway",sans-serif}
.footer{left:0;top:1083px;width:1109px;height:117px;background:var(--footer)}
.footer-links{left:0;width:1118px;top:46px;text-align:center;font-size:11.5px}
.copyright{left:0;width:1118px;top:70px;text-align:center;font-size:9.5px}
.social{top:53px;left:900px;display:flex;gap:21px}
.social span{width:14px;height:14px;border-radius:50%;background:#bdbdbd}
</style>
</head>
<body>
<div class="abs photo-backdrop" role="img" aria-label="Photo of a child in a straw sun hat on a beach under a blue sky"></div>
<div class="abs service-shade"></div>

<header class="abs header">
  <div class="abs brand-panel">
    <span class="brand-name">Brook &amp; Associates</span>
  </div>
  <nav class="abs nav">
    <a class="active" style="left:0">HOME</a>
    <a style="left:79px">ABOUT US</a>
    <a style="left:178px">SERVICES</a>
    <a style="left:274px">CONTACT US</a>
  </nav>
  <div class="abs call">
    <svg width="20" height="20" viewBox="0 0 20 20" aria-hidden="true">
      <path d="M4 3l3 0 1.5 4-2 1.5a10 10 0 0 0 5 5L13 11.5l4 1.5v3c0 1-1 2-2 2C9 18 2 11 2 5c0-1 1-2 2-2z" fill="#fff"/>
      <path d="M12 2a6 6 0 0 1 6 6M12 5a3 3 0 0 1 3 3" stroke="#0aa0f5" stroke-width="1.6" fill="none"/>
    </svg>
    <div>
      <div class="call-label">CALL US</div>
      <div class="call-number">(404) 555-0187</div>
    </div>
  </div>
</header>

<h1 class="abs hero-title">POWERFUL</h1>
<p class="abs hero-sub">Take the Worry out of<br>tax and business</p>
<div class="abs slide-arrow" style="left:47px">
  <svg width="12" height="14" viewBox="0 0 12 14"><path d="M8 2L3 7l5 5" stroke="#fff" stroke-width="2" fill="none"/></svg>
</div>
<div class="abs slide-arrow" style="left:1030px">
  <svg width="12" height="14" viewBox="0 0 12 14"><path d="M4 2l5 5-5 5" stroke="#fff" stroke-width="2" fill="none"/></svg>
</div>

<h2 class="abs section-title" style="top:483px">Our <span>Service</span></h2>

<div class="abs timeline"></div>

<div class="abs service-icon is-current" style="left:168px">
  <svg width="52" height="50" viewBox="0 0 52 50" aria-hidden="true">
    <path d="M14 4h34l-9 38H5z" fill="#1c8fd9"/>
    <path d="M5 42h34l-1 4H5a3 3 0 0 1 0-4z" fill="#1c8fd9"/>
    <path d="M19 13h20M17 20h20" stroke="#fff" stroke-width="3"/>
  </svg>
</div>
<div class="abs service-icon" style="left:491px">
  <svg width="76" height="68" viewBox="0 0 76 68" aria-hidden="true">
    <path d="M30 4h26l10 10v38H30z" fill="none" stroke="#fff" stroke-width="4"/>
    <path d="M44 22h14M44 30h14M44 38h14" stroke="#fff" stroke-width="3"/>
    <circle cx="28" cy="34" r="13" fill="#0aa0f5" stroke="#fff" stroke-width="5"/>
    <path d="M18 44L6 58" stroke="#fff" stroke-width="6" stroke-linecap="round"/>
  </svg>
</div>
<div class="abs service-icon" style="left:790px">
  <svg width="58" height="58" viewBox="0 0 58 58" aria-hidden="true">
    <rect x="4" y="8" width="50" height="46" rx="4" fill="none" stroke="#fff" stroke-width="4"/>
    <rect x="4" y="8" width="50" height="10" fill="#fff"/>
    <rect x="13" y="2" width="5" height="12" rx="2" fill="#fff"/>
    <rect x="40" y="2" width="5" height="12" rx="2" fill="#fff"/>
    <text x="29" y="48" text-anchor="middle" font-family="Raleway,sans-serif" font-weight="700" font-size="25" fill="#fff">15</text>
  </svg>
</div>

<article class="abs service" style="left:65px">
  <h3>TAX PLANNING AND RETURNS</h3>
  <p>Lorem ipsum dolor sit amet, consectetur edit<br>adipiscing elit, sed do eiusmod tempor<br>incididunt utdolore magna aliqua.</p>
  <span class="more is-current">Read More &#9656;</span>
</article>
<article class="abs service" style="left:392px">
  <h3>GST PREPARATION AND LODGEMENT</h3>
  <p>Lorem ipsum dolor sit amet, consectetur edit<br>adipiscing elit, sed do eiusmod tempor<br>incididunt utdolore magna aliqua.</p>
  <span class="more">Read More &#9656;</span>
</article>
<article class="abs service" style="left:685px">
  <h3>LITIGATION ASSISTANCE</h3>
  <p>Lorem ipsum dolor sit amet, consectetur edit<br>adipiscing elit, sed do eiusmod tempor<br>incididunt utdolore a aliqua.</p>
  <span class="more">Read More &#9656;</span>
</article>

<section class="abs newsletter">
  <h2 class="abs section-title">Join Our <span>Newsletter!</span></h2>
  <div class="abs field" style="left:52px;width:358px">Enter Your Name</div>
  <div class="abs field" style="left:434px;width:359px">Enter Your Email id</div>
  <div class="abs signup">SIGN UP</div>
</section>

<footer class="abs footer">
  <div class="abs footer-links">Home&nbsp; / &nbsp;About Us&nbsp; / &nbsp;Services&nbsp; / &nbsp;Contact Us</div>
  <div class="abs copyright">© All Rights Reserved. Copyrights @Brook &amp; Associates. 2015</div>
  <div class="abs social"><span></span><span></span><span></span><span></span><span></span></div>
</footer>
</body>
</html>
```